Auto Repair Specialist needs wordpress design

We are looking for a Word Press website design for a Vantor Truck Service and Repair Specialist shop called Gearhaven. The design should have a slightly retro Industrial feel. You can see our logo and an example of our sign in attached files.

```html
<!DOCTYPE html>
<html lang="en">
<head>
<meta charset="utf-8">
<title>Gearhaven, LLC – Vantor Truck Repair Specialist</title>
<link href="https://fonts.googleapis.com/css2?family=Poppins:wght@400;500;600;700&display=swap" rel="stylesheet">
<style>
:root{
  --blue:#2b3990;
  --blue-deep:#233083;
  --grey:#6a6b70;
  --ink:#222;
  --text:#333;
  --black:#000;
  --white:#fff;
  --star:#f5b400;
  --red:#e0262b;
}
*{box-sizing:border-box;margin:0;padding:0}
html,body{width:1200px;height:3223px;overflow:hidden}
body{position:relative;font-family:'Poppins',sans-serif;color:var(--text);background:var(--white)}
.abs{position:absolute}
.brand{display:flex;align-items:center;gap:10px;font-weight:700;letter-spacing:.5px}
.brand-dot{width:20px;height:20px;border-radius:50%;background:var(--blue);flex:none}
.header .brand{left:76px;top:44px;font-size:20px;color:var(--blue)}
.info{display:flex;align-items:center;gap:10px;font-size:11.5px;line-height:17px;top:52px}
.info strong{color:var(--blue);font-weight:600}
.info svg{flex:none}
.nav{left:0;top:120px;width:1200px;height:66px;background:var(--blue)}
.nav a{position:absolute;top:22px;color:var(--white);font-weight:500;font-size:16px;text-decoration:none;transform:translateX(-50%)}
.hero{left:0;top:186px;width:1200px;height:490px;background:linear-gradient(180deg,#5b66b4 0%,#4552a6 45%,#33418f 100%)}
.hero-title{left:105px;top:268px;color:var(--white);font-size:52px;font-weight:600;line-height:72px}
.hero-sub{left:105px;top:428px;color:var(--white);font-size:16px;font-weight:500}
.btn{display:flex;align-items:center;justify-content:center;gap:12px;background:var(--blue);color:var(--white);font-size:14px;font-weight:500}
.about-mark{left:131px;top:776px;width:370px;height:200px;display:flex;align-items:center;justify-content:center}
.about-mark .brand{font-size:36px;color:var(--blue)}
.about-mark .brand-dot{width:36px;height:36px}
.section-title{color:var(--blue);font-weight:600;font-size:32px;line-height:46px}
.para{font-size:15.5px;line-height:26px;color:var(--text)}
.tile{border-radius:9px;overflow:hidden}
.card-tile{padding:62px 0 0 54px;color:var(--white)}
.card-tile h3{font-size:25px;font-weight:500;margin-bottom:22px}
.card-tile li{font-size:15px;line-height:26px;list-style:none}
.card-tile li::before{content:"•";margin-right:10px;font-size:11px}
.cta{left:0;top:1639px;width:1200px;height:307px;background:linear-gradient(90deg,#1b1c22 0%,#3a2b24 45%,#7a4228 80%,#3a2a28 100%)}
.cta-title{left:0;width:1200px;top:1727px;text-align:center;color:var(--white);font-size:31px;font-weight:600}
.cta-sub{left:0;width:1200px;top:1778px;text-align:center;color:var(--white);font-size:16px;font-weight:500}
.heading{left:0;width:1200px;top:2032px;text-align:center;color:var(--ink);font-size:33px;font-weight:600}
.review{width:226px;height:226px;background:var(--white);border-radius:6px;box-shadow:0 2px 10px rgba(0,0,0,.12);text-align:center;padding-top:46px}
.review h4{font-size:14.5px;font-weight:600;color:var(--ink)}
.stars{color:var(--star);font-size:14px;letter-spacing:3px;margin:3px 0 6px}
.review p{font-size:12.5px;line-height:22px;color:var(--text);padding:0 30px}
.avatar{width:56px;height:56px;border-radius:50%;background:linear-gradient(135deg,#8f8f96,#4a4a55)}
.footer{left:0;top:2915px;width:1200px;height:230px;background:var(--black)}
.footer .brand{color:var(--white);font-size:24px}
.footer .brand-dot{background:var(--white)}
.f-text{color:var(--white);font-size:16px;line-height:26px}
.bottom{left:0;top:3145px;width:1200px;height:78px;background:var(--blue)}
.bottom a{color:var(--white);text-decoration:none;font-size:16px;font-weight:500;margin-right:14px}
</style>
</head>
<body>

<header class="header">
  <div class="abs brand"><span class="brand-dot"></span>GEARHAVEN, LLC</div>
  <div class="abs info" style="left:368px">
    <svg width="34" height="34" viewBox="0 0 34 34"><path d="M3 10l8-3 10 3 8-3v20l-8 3-10-3-8 3z" fill="var(--blue)"/><circle cx="25" cy="8" r="6" fill="var(--white)" stroke="var(--blue)" stroke-width="2.5"/><circle cx="25" cy="8" r="2" fill="var(--blue)"/></svg>
    <div><strong>GEARHAVEN, LLC REPAIR SERVICE CENTER</strong><br>Your Location here</div>
  </div>
  <div class="abs info" style="left:726px">
    <svg width="22" height="34" viewBox="0 0 22 34"><rect x="2" y="2" width="18" height="30" rx="3" fill="none" stroke="var(--blue)" stroke-width="2.5"/><line x1="8" y1="27" x2="14" y2="27" stroke="var(--blue)" stroke-width="2"/></svg>
    <div>Call us Now!</div>
  </div>
  <div class="abs info" style="left:893px">
    <svg width="40" height="38" viewBox="0 0 40 38"><circle cx="17" cy="17" r="15" fill="none" stroke="var(--blue)" stroke-width="3"/><path d="M17 8v9h7" stroke="var(--blue)" stroke-width="3" fill="none"/><rect x="24" y="24" width="14" height="12" fill="var(--blue)"/></svg>
    <div><strong>MONDAY - FRIDAY</strong><br>7:30 AM - 5:00 PM</div>
  </div>
</header>

<nav class="abs nav">
  <a href="#" style="left:373px">HOME</a>
  <a href="#" style="left:501px">SERVICES</a>
  <a href="#" style="left:653px">ABOUT US</a>
  <a href="#" style="left:810px">CONTACT</a>
</nav>

<section class="abs hero" role="img" aria-label="Blue pickup truck on rocky ground in misty landscape, tinted blue"></section>
<h1 class="abs hero-title">VANTOR TRUCK<br>REPAIR SPECIALIST</h1>
<p class="abs hero-sub">GIVE US A CALL WE ARE HAPPY TO ASSIST YOU.</p>
<div class="abs btn" style="left:111px;top:489px;width:170px;height:55px">
  <svg width="16" height="24" viewBox="0 0 16 24"><rect x="1.5" y="1.5" width="13" height="21" rx="2" fill="none" stroke="#fff" stroke-width="2"/><line x1="6" y1="19" x2="10" y2="19" stroke="#fff" stroke-width="1.5"/></svg>000-446-222
</div>

<div class="abs about-mark"><div class="brand"><span class="brand-dot"></span>GEARHAVEN, LLC</div></div>
<h2 class="abs section-title" style="left:609px;top:797px">GEARHAVEN, LLC</h2>
<p class="abs para" style="left:609px;top:854px;width:460px">Lorem ipsum dolor sit amet consectetur. Adipiscing suspendisse et etiam maecenas. Ultrices ornare sed vel bibendum donec duis. Tristique convallis urna duis augue at non fames. Tempor mauris amet nibh enim tortor sem viverra euismod.</p>

<div class="abs tile card-tile" style="left:129px;top:1057px;width:309px;height:229px;background:var(--blue)">
  <svg class="abs" style="left:222px;top:30px" width="54" height="56" viewBox="0 0 54 56"><circle cx="18" cy="28" r="13" fill="none" stroke="#fff" stroke-width="8" stroke-dasharray="7 4"/><path d="M36 6v14M46 6v14M36 20h10v30h-10z" stroke="#fff" stroke-width="5" fill="none"/></svg>
  <h3>REPAIR</h3>
  <ul><li>Brake pad services</li><li>Engine services</li><li>Spark plugs services</li></ul>
</div>
<div class="abs tile" style="left:445px;top:1057px;width:310px;height:229px;background:linear-gradient(180deg,#c9ccd6 0%,#6e7280 40%,#1e2028 100%)" role="img" aria-label="Driver's hands on truck steering wheel with city skyline ahead"></div>
<div class="abs tile card-tile" style="left:762px;top:1057px;width:309px;height:229px;background:var(--grey)">
  <h3>VANTOR SERVICE</h3>
  <ul><li>Multi-point inspection</li><li>Tire rotation</li></ul>
</div>
<div class="abs tile" style="left:133px;top:1305px;width:310px;height:230px;background:linear-gradient(135deg,#3a3d48 0%,#22252d 60%,#9a9ca4 100%)" role="img" aria-label="Mechanic in gloves working on an engine with a wrench"></div>
<div class="abs tile card-tile" style="left:448px;top:1305px;width:309px;height:230px;background:var(--blue)">
  <h3>SALES</h3>
  <ul><li>Vantor Sparepart</li><li>Tire</li></ul>
</div>
<div class="abs tile" style="left:762px;top:1305px;width:309px;height:230px;background:linear-gradient(135deg,#c66a2a 0%,#4a4d56 50%,#e6e8ec 100%)" role="img" aria-label="Gloved hands inspecting a car engine bay"></div>

<section class="abs cta" role="img" aria-label="Mechanic working beside a truck tire in warm workshop light"></section>
<h2 class="abs cta-title">Lorem ipsum dolor sit amet consectetur.</h2>
<p class="abs cta-sub">GIVE US A CALL WE ARE HAPPY TO ASSIST YOU.</p>
<div class="abs btn" style="left:499px;top:1821px;width:172px;height:54px">
  <svg width="16" height="24" viewBox="0 0 16 24"><rect x="1.5" y="1.5" width="13" height="21" rx="2" fill="none" stroke="#fff" stroke-width="2"/><line x1="6" y1="19" x2="10" y2="19" stroke="#fff" stroke-width="1.5"/></svg>000-446-222
</div>

<h2 class="abs heading">WHAT OUR CUSTOMERS ARE SAYING</h2>
<svg class="abs" style="left:156px;top:2255px" width="16" height="22" viewBox="0 0 16 22"><path d="M12 2L3 11l9 9" stroke="#222" stroke-width="2" fill="none"/></svg>
<svg class="abs" style="left:1010px;top:2255px" width="16" height="22" viewBox="0 0 16 22"><path d="M4 2l9 9-9 9" stroke="#222" stroke-width="2" fill="none"/></svg>

<div class="abs review" style="left:219px;top:2158px"><h4>Marco Velletri</h4><div class="stars">★★★★★</div><p>Lorem ipsum dolor sit amet consectetur. Cras viverra id ac proin amet. Donec laoreet gravida et.</p></div>
<div class="abs review" style="left:475px;top:2158px"><h4>Danielle</h4><div class="stars">★★★★★</div><p>Lorem ipsum dolor sit amet consectetur. Cras viverra id ac proin amet. Donec laoreet gravida et.</p></div>
<div class="abs review" style="left:731px;top:2158px"><h4>Tomas Reed</h4><div class="stars">★★★★★</div><p>Lorem ipsum dolor sit amet consectetur. Cras viverra id ac proin amet. Donec laoreet gravida et.</p></div>
<div class="abs avatar" style="left:298px;top:2137px" role="img" aria-label="Customer portrait"></div>
<div class="abs avatar" style="left:554px;top:2137px" role="img" aria-label="Customer portrait"></div>
<div class="abs avatar" style="left:810px;top:2137px" role="img" aria-label="Customer portrait"></div>

<h2 class="abs section-title" style="left:154px;top:2508px">RELIABLE TRUCK, RELIABLE<br>AUTO REPAIR SHOP</h2>
<p class="abs para" style="left:154px;top:2620px;width:460px">Lorem ipsum dolor sit amet consectetur. Adipiscing suspendisse et etiam maecenas. Ultrices ornare sed vel bibendum donec duis. Tristique convallis urna duis augue at non fames. Tempor mauris amet nibh enim tortor sem viverra euismod.</p>
<div class="abs btn" style="left:148px;top:2772px;width:171px;height:54px">
  <svg width="16" height="24" viewBox="0 0 16 24"><rect x="1.5" y="1.5" width="13" height="21" rx="2" fill="none" stroke="#fff" stroke-width="2"/><line x1="6" y1="19" x2="10" y2="19" stroke="#fff" stroke-width="1.5"/></svg>000-446-222
</div>
<div class="abs" style="left:723px;top:2475px;width:320px;height:320px;border-radius:50%;border:4px solid var(--blue);background:linear-gradient(180deg,#d8d6d2 0%,#9a8f82 40%,#7b7064 100%)" role="img" aria-label="Mechanic lying under a vehicle with tools beside him"></div>

<footer class="abs footer">
  <div class="abs brand" style="left:126px;top:100px"><span class="brand-dot"></span>GEARHAVEN, LLC</div>
  <svg class="abs" style="left:458px;top:54px" width="28" height="28" viewBox="0 0 28 28"><path d="M6 3l5 5-3 4c2 4 5 7 9 9l4-3 5 5-4 4C12 26 2 16 2 7z" fill="none" stroke="var(--red)" stroke-width="2"/></svg>
  <div class="abs f-text" style="left:502px;top:50px">Contact Us<br>000-2222-000</div>
  <svg class="abs" style="left:740px;top:54px" width="26" height="26" viewBox="0 0 26 26"><circle cx="13" cy="13" r="11" fill="none" stroke="var(--red)" stroke-width="2"/><path d="M13 6v7h5" stroke="var(--red)" stroke-width="2" fill="none"/></svg>
  <div class="abs f-text" style="left:776px;top:50px"><b style="font-weight:500">Hours:</b><br>Monday - Thursday:&nbsp; 8:00am - 5:00pm<br>Friday:&nbsp; 8:00am - 4:00pm<br>Saturday - Sunday:&nbsp; Closed</div>
</footer>

<div class="abs bottom">
  <div class="abs" style="left:157px;top:21px"><a href="#">HOME</a><a href="#">SERVICES</a><a href="#">ABOUT US</a><a href="#">CONTACT US</a></div>
  <div class="abs f-text" style="right:140px;top:21px">© Copyright 2023 by Gearhaven, LLC</div>
</div>

</body>
</html>
```